Author of female self help book in need of cover that expresses freedom and empowerment

This is the first in a series of female self help books. It is called Her Quiet Lantern. The book tells my story of hitting rock bottom, winning the lottery, and discovering what I call my Quiet Lantern. The purpose of the book is to help inspire women to break free from the pain of loss including divorce, job loss, or heartbreak. It will help guide a women's journey to finding their courage and motivation to move on in pursuit of happiness and joy. She will gain skills to help build resilience, tap into her inner strength, achieve success in her personal and professional life and finally create a life she loves to live.

Target Market(s)

Women 30-60 yrs, divorced, single mother, widow, working professional

Industry/Entity Type

Life Coaching

Font styles to use
Serif

Colors
fbd4d5
f59296

Requirements
Must have
• Cover must express female freedom and empowerment.
Nice to have
• I would like to see something like a mountain top scene or woman depicted with arms raised high in victory.

```html
<!DOCTYPE html>
<html lang="en">
<head>
<meta charset="utf-8">
<title>Her Quiet Lantern — Book Cover</title>
<link rel="stylesheet" href="https://fonts.googleapis.com/css2?family=Playfair+Display:wght@400&family=Great+Vibes&family=Poppins:wght@300;600&display=swap">
<style>
  :root {
    --page: #ffffff;
    --blush-light: #fdf3f4;
    --blush: #fbd4d5;
    --rose: #f59296;
    --mauve: #d98fc0;
    --glow: #ffc56b;
    --plum: #5b1f7a;
    --ink: #4a4a4a;
  }
  html, body {
    margin: 0;
    width: 1200px;
    height: 1200px;
    overflow: hidden;
    background: var(--page);
  }
  .canvas {
    position: relative;
    width: 1200px;
    height: 1200px;
  }
  .cover {
    position: absolute;
    left: 170px;
    top: 45px;
    width: 860px;
    height: 1110px;
    overflow: hidden;
    box-shadow: 0 2px 6px rgba(0,0,0,0.15);
  }
  .cover-art {
    position: absolute;
    inset: 0;
    background:
      radial-gradient(ellipse 260px 120px at 18% 50%, rgba(255,197,107,0.75), rgba(255,197,107,0) 70%),
      radial-gradient(ellipse 200px 160px at 92% 60%, rgba(255,220,150,0.55), rgba(255,220,150,0) 70%),
      radial-gradient(ellipse 230px 520px at 22% 78%, rgba(217,143,192,0.55), rgba(217,143,192,0) 70%),
      linear-gradient(180deg, var(--page) 0%, var(--blush-light) 38%, var(--blush) 72%, #ecb0cf 100%);
  }
  .cover-text {
    position: absolute;
    right: 56px;
    text-align: right;
    margin: 0;
  }
  .tagline {
    top: 365px;
    font-family: "Poppins", sans-serif;
    font-weight: 300;
    font-size: 27px;
    line-height: 1.25;
    color: var(--ink);
  }
  .tagline strong, .subtitle strong {
    font-weight: 600;
  }
  .title {
    top: 455px;
    color: var(--plum);
    font-weight: 400;
  }
  .title-serif {
    display: block;
    font-family: "Playfair Display", serif;
    font-size: 98px;
    line-height: 1;
  }
  .title-script {
    display: block;
    font-family: "Great Vibes", cursive;
    font-size: 175px;
    line-height: 0.9;
    margin-top: 40px;
    margin-right: -20px;
  }
  .subtitle {
    top: 805px;
    font-family: "Poppins", sans-serif;
    font-weight: 300;
    font-size: 27px;
    line-height: 1.3;
    color: var(--ink);
  }
  .author {
    top: 945px;
  }
  .author-name {
    display: block;
    font-family: "Playfair Display", serif;
    font-size: 46px;
    color: var(--plum);
    line-height: 1.1;
  }
  .author-role {
    display: block;
    font-family: "Poppins", sans-serif;
    font-weight: 300;
    font-size: 15px;
    color: var(--ink);
    margin-top: 4px;
  }
</style>
</head>
<body>
<div class="canvas">
  <section class="cover">
    <div class="cover-art" role="img" aria-label="Soft pink sunrise photo of a woman in a flowing dress standing in shallow water with arms raised, orange birds flying overhead"></div>

    <p class="cover-text tagline">Rock bottom is where she found the<br><strong>KEYS TO UNLOCKING</strong></p>

    <h1 class="cover-text title">
      <span class="title-serif">Her Quiet</span>
      <span class="title-script">Lantern</span>
    </h1>

    <p class="cover-text subtitle">And that led her on a remarkable<br>journey to <strong>ACHIEVING SUCCESS!</strong></p>

    <p class="cover-text author">
      <span class="author-name">Mara Ellison,</span>
      <span class="author-role">Author, Life Strategist, Success Coach</span>
    </p>
  </section>
</div>
</body>
</html>
```